International Sustainable Cities NGO needs PPT Design

We need a PPT design for a presentation upcoming at a leading university on the East coast. The design needs to be clean and simple, professional and room for photos and maps. It's a presentation about citizen mapping and data collection for city planning/decision making.

University

```html
<!DOCTYPE html>
<html lang="en">
<head>
<meta charset="utf-8">
<title>Civiscope – Presentation Overview</title>
<link href="https://fonts.googleapis.com/css2?family=Carlito:wght@400;700&display=swap" rel="stylesheet">
<style>
  :root {
    --bg-center: #fbfbfb;
    --bg-mid: #dcdcdc;
    --bg-edge: #9c9c9c;
    --corner-block: #8a8a8a;
    --name-ink: #2a2a2a;
    --title-ink: #111111;
    --subtitle-ink: #1c1c1c;
    --body-ink: #3f3f3f;
    --body-ink-soft: #4a4a4a;
    --bullet: #555555;
    --rule-dark: #5e5e5e;
    --rule-light: #8c8c8c;
  }
  * { margin: 0; padding: 0; box-sizing: border-box; }
  html, body { width: 1200px; height: 675px; overflow: hidden; }
  body { font-family: "Carlito", Calibri, Arial, sans-serif; background: var(--bg-mid); }

  .slide {
    position: relative;
    width: 1200px;
    height: 675px;
    overflow: hidden;
    background: radial-gradient(ellipse 75% 80% at 50% 35%, var(--bg-center) 0%, var(--bg-mid) 60%, var(--bg-edge) 100%);
  }

  .corner-block {
    position: absolute;
    top: 38px;
    width: 65px;
    height: 72px;
    background: linear-gradient(180deg, #a3a3a3, var(--corner-block));
    opacity: 0.75;
  }
  .corner-block--left { left: 0; }
  .corner-block--right { right: 0; }

  .org-name,
  .partner-name {
    position: absolute;
    top: 64px;
    display: flex;
    align-items: center;
    gap: 10px;
    font-weight: 700;
    font-size: 30px;
    line-height: 34px;
    color: var(--name-ink);
  }
  .org-name { left: 84px; }
  .partner-name { right: 80px; }
  .org-name .mark {
    width: 12px;
    height: 12px;
    background: var(--name-ink);
  }
  .partner-name .mark {
    width: 12px;
    height: 12px;
    border-radius: 50%;
    background: var(--name-ink);
  }

  .content {
    position: absolute;
    left: 69px;
    top: 163px;
    width: 1066px;
  }
  .slide-title {
    font-weight: 700;
    font-size: 38px;
    line-height: 46px;
    color: var(--title-ink);
  }
  .slide-subtitle {
    margin-top: 11px;
    font-weight: 700;
    font-size: 21.5px;
    line-height: 28px;
    color: var(--subtitle-ink);
  }

  .summary {
    position: relative;
    margin-top: 6px;
    padding-left: 35px;
    font-size: 21px;
    line-height: 27.5px;
  }
  .summary .bullet {
    position: absolute;
    left: 9px;
    top: 8px;
    width: 9px;
    height: 12px;
  }
  .summary p { color: var(--body-ink); }
  .summary p + p { margin-top: 3px; color: var(--body-ink-soft); }
  .summary .closing { font-size: 22px; color: var(--body-ink); }

  .bottom-rule {
    position: absolute;
    left: 70px;
    top: 631px;
    width: 1084px;
    height: 6px;
    background: linear-gradient(180deg, var(--rule-light), var(--rule-dark));
  }
</style>
</head>
<body>
<main class="slide">
  <div class="corner-block corner-block--left"></div>
  <div class="corner-block corner-block--right"></div>

  <div class="org-name"><span class="mark"></span>Greenward Commons</div>
  <div class="partner-name"><span class="mark"></span>Civiscope</div>

  <section class="content">
    <h1 class="slide-title">This is what the presentation is about</h1>
    <h2 class="slide-subtitle">Civiscope – Geospatial Mapping and Education for Community Sustainability and Resilience</h2>

    <div class="summary">
      <svg class="bullet" viewBox="0 0 9 12" aria-hidden="true"><path d="M0 0 L9 6 L0 12 Z" fill="var(--bullet)"/></svg>
      <p>This presentation will introduce an interdisciplinary, educational and participatory approach to neighborhood and city-level data collection, management and visualization that supports community-led strategies for urban sustainability and resilience. Highlighted will be processes that integrate environmental, social and economic data for an urban area and its surrounding region, providing a common visual language that facilitates discussion between local stakeholders and government agencies.</p>
      <p>Current Latin American case studies under the Office of Regional Studies’ Growing Cities Program will be showcased, including a low income community of Medellin, Colombia, and an historic neighborhood in Cusco, Peru. Topics covered will include a discussion of mapping technologies selected and piloted and their advantages and disadvantages, the challenges and successes of participatory mapping in the case study locations, and conclusions drawn thus far <span class="closing">from the experience.</span></p>
    </div>
  </section>

  <div class="bottom-rule"></div>
</main>
</body>
</html>
```